High Quality Hemp Flowers Packaging Design

We need a logo and packaging design for a new CBD hemp product. We sell CBD rich hemp flower- tops to our customers in Europe. CBD's natural benefits are extensive and generally used for all sorts of reasons.
Our strains are of the highest quality and used as an aromatic product. Thus the design should look clean and modern with a slight organic touch. We'd like people to associate our product with a luxury product like a good wine or whiskey but still being modern, healthy and organic.
The product comes in a brown cardboard paper tube and the design needs to include:
-our logo made of the "vesko amulett" (attachment 1 vesko amulett)
-our website: "tobrinu.eu"
-the product name: "vesko"
tube properties:
tube size: 6cm diameter, 7cm height (please see attachment 2 Paper Tube 6cm diameter, 7cm height. jpg)
• material: 2mm thickness cardboard+brown kraft paper (like in attachment 3 Paper Tube colour.jpg – picture just a sample for the material – size is not correctly displayed in this picture)
• coated aluminum foil paper inside
• colour/ product name: whatever colour and where ever you want to place it in your design
• colour/ vesko amulet logo: whatever colour and where ever you want to place it in your design
• sticker (2-2.5 x 5-6,5cm –> whatever the designer thinks works better) for sealing use, to keep the two parts of the tube together and it needs to have a placeholder for the date of the packaging (like in attachment 2 Paper Tube 6cm diameter 7cm height – but the sticker will not cover the full side of the tube as in attachment 2, but just 5-6.5 cm)
• “inner” tube could be color printing (for clarification which part please see attachment 3 Paper Tube colour.jpg -> the white part – picture just a sample for the “white part” – size is not correctly displayed in this picture
- We dont need any marihuana leafs or signs.

```html
<!DOCTYPE html>
<html lang="en">
<head>
<meta charset="utf-8">
<title>vesko – CBD Rich Hemp Flower Tube Label</title>
<link rel="stylesheet" href="https://fonts.googleapis.com/css2?family=Open+Sans:wght@400;600;700&display=swap">
<style>
  :root {
    --page-bg: #ffffff;
    --kraft: #c49b6e;
    --kraft-light: #d0a97d;
    --leaf-deep: #2f5a2c;
    --leaf-mid: #4f8a3e;
    --leaf-soft: #7fae62;
    --gold-dark: #a8761f;
    --gold-mid: #e1b551;
    --gold-light: #f8e3a0;
    --ink: #1c1a17;
  }
  * { box-sizing: border-box; margin: 0; padding: 0; }
  html, body {
    width: 1200px;
    height: 1200px;
    overflow: hidden;
    background: var(--page-bg);
  }
  .canvas {
    position: relative;
    width: 1200px;
    height: 1200px;
  }
  .tube-label {
    position: absolute;
    left: 410px;
    top: 160px;
    width: 380px;
    height: 880px;
    background: linear-gradient(90deg, var(--kraft) 0%, var(--kraft-light) 50%, var(--kraft) 100%);
    overflow: hidden;
    font-family: "Open Sans", Arial, sans-serif;
  }
  .plant-visual {
    position: absolute;
    left: 0; top: 0;
    width: 100%;
    height: 305px;
    background:
      radial-gradient(ellipse 60% 55% at 50% 45%, var(--leaf-soft) 0%, var(--leaf-mid) 45%, transparent 80%),
      linear-gradient(180deg, var(--leaf-mid) 0%, var(--leaf-deep) 100%);
  }
  .gold-band {
    position: absolute;
    left: 0;
    width: 100%;
    background: linear-gradient(90deg, var(--gold-dark) 0%, var(--gold-mid) 25%, var(--gold-light) 50%, var(--gold-mid) 75%, var(--gold-dark) 100%);
  }
  .product-band {
    top: 305px;
    height: 68px;
    display: flex;
    align-items: center;
    justify-content: center;
  }
  .product-band .product-title {
    font-size: 29px;
    font-weight: 400;
    letter-spacing: 0.5px;
    color: var(--ink);
    white-space: nowrap;
  }
  .seal-band {
    top: 541px;
    height: 72px;
  }
  .brand-seal {
    position: absolute;
    left: 46px;
    top: 436px;
    width: 288px;
    height: 288px;
    border-radius: 50%;
    background: radial-gradient(circle at 40% 35%, var(--gold-light) 0%, var(--gold-mid) 55%, var(--gold-dark) 100%);
    display: flex;
    align-items: center;
    justify-content: center;
  }
  .brand-seal .brand-name {
    font-size: 62px;
    font-weight: 700;
    color: var(--ink);
  }
  .web-band {
    top: 787px;
    height: 34px;
    display: flex;
    align-items: center;
    justify-content: center;
  }
  .web-band .web-address {
    font-size: 21px;
    font-weight: 400;
    letter-spacing: 0.5px;
    color: var(--ink);
  }
</style>
</head>
<body>
  <main class="canvas">
    <section class="tube-label">
      <div class="plant-visual" role="img" aria-label="Close-up photograph of a green hemp plant top"></div>
      <div class="gold-band product-band">
        <h1 class="product-title">CBD RICH HEMP FLOWER</h1>
      </div>
      <div class="gold-band seal-band"></div>
      <div class="brand-seal">
        <span class="brand-name">vesko</span>
      </div>
      <div class="gold-band web-band">
        <span class="web-address">www.tobrinu.eu</span>
      </div>
    </section>
  </main>
</body>
</html>
```